Flyer-Design für innovativen Anbieter von E-Mobilität
Zielgruppe
Wir sind ein innovativer Anbieter von E-Mobilität und bieten Erlebnisse, Seminare und Fahrzeugmieten an. Unsere Zielgruppe sind Endverbraucher, die oftmals noch keine größere Erfahrung mit E-Mobilität haben, diese aber kennenlernen wollen. Darüber hinaus sind auch Touristen und Besucher unsere Zielgruppe.
Aufgabenstellung
Der Flyer sollte zwingend das Thema Ökologie/Nachhaltigkeit berücksichtigen. Zudem soll es emotional ansprechend sein. Bei den Texten liegt eine Vorlage anbei, wobei wir gerne auch einen neuen Ansatz verfolgen würden. Der Flyer sollte in Deutsch und Englisch gehalten sein.

```html
<!DOCTYPE html>
<html lang="de">
<head>
<meta charset="utf-8">
<title>Voltwerk – Erlebnisse &amp; Seminare Flyer</title>
<link href="https://fonts.googleapis.com/css2?family=Archivo+Black&family=Arimo:ital,wght@0,400;0,700;1,400;1,700&display=swap" rel="stylesheet">
<style>
:root{
  --green:#6cb84a;
  --blue:#2f5da8;
  --blue-soft:#7f8fc4;
  --paper:#f6f6f4;
  --ink:#333;
  --grey:#9a9a9a;
  --bg:#c3d8b8;
  --url-band:#e9e9e6;
}
*{box-sizing:border-box;margin:0;padding:0}
html,body{width:1200px;height:947px;overflow:hidden;background:var(--bg);font-family:"Arimo",Arial,sans-serif;color:var(--ink)}
.canvas{position:relative;width:1200px;height:947px}
.spread{position:absolute;top:276px;display:flex;box-shadow:0 6px 18px rgba(0,0,0,.18)}
.spread--outer{left:24px}
.spread--inner{left:618px}
.panel{position:relative;width:186px;height:394px;background:var(--paper);overflow:hidden;border-right:1px solid #e4e4e0}
.panel:last-child{border-right:none}
.head{font-family:"Archivo Black","Arimo",sans-serif;font-size:9px;line-height:1.15;color:var(--blue);text-transform:uppercase}
.head em{display:block;font-style:italic;color:var(--blue-soft);font-family:"Arimo",sans-serif;font-weight:700}
.txt{font-size:5.6px;line-height:1.35;color:var(--ink)}
.txt--en{color:var(--grey)}
.url{position:absolute;left:0;right:0;bottom:0;height:22px;background:var(--url-band);font-size:7px;font-weight:700;color:#555;display:flex;align-items:center;padding-left:12px}
.photo{position:absolute;border-radius:3px}
.photo--showroom{background:linear-gradient(135deg,#dcdcd8,#8d8f8c 60%,#c9a48b)}
.photo--car{background:linear-gradient(160deg,#cfd6dc,#4a4e50 70%,#2f3133)}
.photo--bike{background:linear-gradient(160deg,#c9d8e6,#8a8f8c 60%,#6f8a5c)}
.photo--map{background:linear-gradient(135deg,#eceeea,#b9dcae 50%,#e7e7e2)}
.photo--tree{background:radial-gradient(circle,#7fc35a,#6cb84a 60%,transparent 62%)}
.car-icon{position:absolute;width:16px;height:10px}
.offer{position:absolute;left:0;right:0;height:120px}
.offer__bar{position:absolute;left:0;top:0;width:44px;height:100%;background:var(--green)}
.offer__tag{position:absolute;left:44px;top:0;right:74px;height:12px;background:var(--green);color:#fff;font-size:5.5px;font-weight:700;padding:3px 4px}
.offer .photo{left:12px;top:12px;width:70px;height:62px;border-radius:0}
.offer__info{position:absolute;left:92px;top:16px;right:8px}
.offer__title{font-size:6px;color:var(--blue-soft);font-weight:700;border-bottom:1px solid #ddd;padding-bottom:2px;margin-bottom:3px}
.offer__price{font-size:9px;color:var(--blue);margin-top:4px}
.offer__price small{font-size:4.5px;color:var(--blue-soft);margin-right:4px}
.brand{font-family:"Arimo",sans-serif;font-weight:700;color:var(--green);font-size:19px;display:flex;align-items:center;gap:5px}
.brand::before{content:"";width:9px;height:9px;border-radius:50%;background:var(--blue)}
.brand-sub{font-size:5.5px;color:var(--blue);font-weight:700}
.cover-top{position:absolute;left:0;top:0;width:100%;height:252px;background:var(--green)}
.cover-title{position:absolute;left:14px;top:84px;font-family:"Archivo Black",sans-serif;color:#fff;font-size:24px;line-height:1.05}
.cover-sub{position:absolute;left:14px;top:140px;color:#fff;font-size:13px;font-weight:700}
.cover-word{position:absolute;color:#fff;font-size:6px}
.cover-badge{position:absolute;left:0;top:222px;width:158px;height:52px;background:var(--blue);border-radius:0 8px 8px 0;color:#fff;font-family:"Archivo Black",sans-serif;font-size:12px;line-height:1.1;padding:8px 10px}
.cover-tag{position:absolute;left:12px;top:282px;font-size:9px;color:#555}
.booking{position:absolute;left:0;top:222px;width:168px;height:34px;background:var(--green);border-radius:0 8px 8px 0;color:#fff;font-family:"Archivo Black",sans-serif;font-size:7px;padding:7px 10px;line-height:1.35}
.claim{position:absolute;left:14px;top:30px;right:10px;font-size:8px;font-weight:700;color:#444}
.claim em{display:block;font-size:7px;color:var(--grey);margin-top:3px}
</style>
</head>
<body>
<div class="canvas">

  <svg width="0" height="0" style="position:absolute">
    <defs>
      <symbol id="car" viewBox="0 0 16 10"><path d="M2 5 L4 1.5 H11 L13.5 5 H15 V8 H1 V5Z" fill="#2f5da8"/><circle cx="4.5" cy="8.3" r="1.6" fill="#2f5da8" stroke="#fff" stroke-width=".6"/><circle cx="11.5" cy="8.3" r="1.6" fill="#2f5da8" stroke="#fff" stroke-width=".6"/><rect x="5" y="2.3" width="2.6" height="2.2" fill="#fff"/><rect x="8.3" y="2.3" width="2.6" height="2.2" fill="#fff"/></symbol>
    </defs>
  </svg>

  <section class="spread spread--outer">
    <article class="panel">
      <h2 class="head" style="position:absolute;left:12px;top:18px;right:10px">Voltwerk, das sind wir<em>Voltwerk, this is us</em></h2>
      <p class="txt" style="position:absolute;left:12px;top:50px;right:12px">Hier kann ein Text noch genau zur Firma stehen, auch zu Voltwerk. Über ein paar Zeilen, als Einleitung für den Flyer.</p>
      <p class="txt txt--en" style="position:absolute;left:12px;top:74px;right:12px">Here a short text about the company can be placed, a few lines as an introduction to the flyer.</p>
      <div class="photo photo--showroom" role="img" aria-label="Elektroauto an einer Ladesäule im Showroom" style="left:12px;top:104px;width:162px;height:112px"></div>
      <p class="txt" style="position:absolute;left:12px;top:226px;right:12px">Lernen Sie die Möglichkeiten nachhaltiger und ökologischer Mobilität kennen und schätzen. Ohne Markenbindung. Ganz wie Sie es wollen.</p>
      <p class="txt txt--en" style="position:absolute;left:12px;top:258px;right:12px">Get known to the wide possibilities of sustainable and ecological mobility, enjoy them and let them convince you! Just as you like.</p>
      <svg class="car-icon" style="left:12px;top:340px"><use href="#car"/></svg>
      <svg class="car-icon" style="left:160px;top:350px"><use href="#car"/></svg>
      <div class="url">www.voltwerk-erleben.com</div>
    </article>

    <article class="panel">
      <div class="brand" style="position:absolute;left:12px;top:20px">Voltwerk</div>
      <div class="brand-sub" style="position:absolute;left:28px;top:44px">future mobility solutions · by Fahrwerk Mobil</div>
      <p class="txt" style="position:absolute;left:12px;top:62px;right:10px">Fon / Phone: +49 69 555 0142<br>E-Mail: hallo@voltwerk-erleben.de</p>
      <p class="txt" style="position:absolute;left:12px;top:86px;right:10px">Wo? Zentraler geht es kaum:<br><span class="txt--en">Where? Just in the center of town:</span></p>
      <div class="photo photo--map" role="img" aria-label="Stadtplan mit Standortmarkierung am Lindenhof-Quartier" style="left:12px;top:110px;width:160px;height:104px"></div>
      <div class="booking">BUCHUNGEN &amp; INFO UNTER<br>www.voltwerk-erleben.de</div>
      <p class="txt" style="position:absolute;left:12px;top:268px;right:10px">Das neue Lindenhof-Quartier erreichen Sie sehr bequem per S-Bahn (S4), Bus (42/47), Regionalzug (Bahnhof Lindenhof Süd) oder auch per Auto (gebührenpflichtige Parkplätze ausreichend vorhanden).</p>
      <p class="txt txt--en" style="position:absolute;left:12px;top:312px;right:10px">Lindenhof-Quartier is reachable via S-Bahn (S4), bus (42/47), train (station „Lindenhof Süd“) or car (parking lots available at a charge).</p>
      <svg class="car-icon" style="left:156px;top:350px"><use href="#car"/></svg>
      <div class="url">www.voltwerk-erleben.com</div>
    </article>

    <article class="panel">
      <div class="cover-top"></div>
      <span class="cover-word" style="left:108px;top:24px">erfassen.</span>
      <span class="cover-word" style="left:122px;top:40px">electrifying.</span>
      <h1 class="cover-title">E-<br>MOBILITÄT.</h1>
      <div class="cover-sub">e-mobility.</div>
      <span class="cover-word" style="left:60px;top:172px">erleben.</span>
      <span class="cover-word" style="left:118px;top:180px">experience.</span>
      <span class="cover-word" style="left:20px;top:194px">einfach.</span>
      <span class="cover-word" style="left:62px;top:202px">easy.</span>
      <span class="cover-word" style="left:140px;top:206px">engage.</span>
      <div class="cover-badge">ERLEBNISSE &amp;<br>SEMINARE</div>
      <div class="cover-tag">Experiences &amp; workshops</div>
      <div class="brand" style="position:absolute;left:22px;top:326px">Voltwerk</div>
      <div class="brand-sub" style="position:absolute;left:38px;top:350px">future mobility solutions · by Fahrwerk Mobil</div>
    </article>
  </section>

  <section class="spread spread--inner">
    <article class="panel">
      <h2 class="head" style="position:absolute;left:12px;top:16px;right:8px">Erlebnisse &amp; Seminare<em>Experiences &amp; workshops</em></h2>
      <p class="txt" style="position:absolute;left:12px;top:44px;right:10px">Einleitung zu den folgenden Seminaren und Möglichkeiten. Text in deutsch und englisch.</p>
      <p class="txt txt--en" style="position:absolute;left:12px;top:60px;right:10px">Introduction to the following seminars and options. Text in German and English.</p>
      <div class="offer" style="top:84px">
        <div class="offer__bar"></div><div class="offer__tag">Erlebnisprobefahrt</div>
        <div class="photo photo--car" role="img" aria-label="Elektroauto auf einer Landstraße"></div>
        <div class="offer__info"><div class="offer__title">Adventure test e-drive</div><p class="txt">Diverse Modelle stehen für Ihr besonderes Erlebnis zur Verfügung.</p><p class="txt txt--en">Many car models at your disposal.</p><div class="offer__price"><small>ab / from</small>29,00 EUR</div></div>
      </div>
      <div class="offer" style="top:210px">
        <div class="offer__bar"></div><div class="offer__tag">Miete ein e-bike</div>
        <div class="photo photo--bike" role="img" aria-label="Elektrofahrrad im Grünen"></div>
        <div class="offer__info"><div class="offer__title">Rent a e-bike</div><p class="txt">Einfach mal raus – bequem per eBike</p><p class="txt txt--en">Just get out – but comfortable with your ebike</p><div class="offer__price"><small>ab / from</small>9,00 EUR</div></div>
      </div>
      <svg class="car-icon" style="left:14px;top:350px"><use href="#car"/></svg>
    </article>

    <article class="panel">
      <div class="offer" style="top:30px">
        <div class="offer__bar"></div><div class="offer__tag">Erlebnisprobefahrt</div>
        <div class="photo photo--car" role="img" aria-label="Elektroauto auf einer Landstraße"></div>
        <div class="offer__info"><div class="offer__title">Adventure test e-drive</div><p class="txt">Diverse Modelle stehen für Ihr besonderes Erlebnis zur Verfügung.</p><p class="txt txt--en">Many car models at your disposal.</p><div class="offer__price"><small>ab / from</small>29,00 EUR</div></div>
      </div>
      <div class="offer" style="top:156px">
        <div class="offer__bar"></div><div class="offer__tag">Miete ein e-bike</div>
        <div class="photo photo--bike" role="img" aria-label="Elektrofahrrad im Grünen"></div>
        <div class="offer__info"><div class="offer__title">Rent a e-bike</div><p class="txt">Einfach mal raus – bequem per eBike</p><p class="txt txt--en">Just get out – but comfortable with your ebike</p><div class="offer__price"><small>ab / from</small>9,00 EUR</div></div>
      </div>
      <div class="photo photo--tree" role="img" aria-label="Grüner Baum als Symbol für Nachhaltigkeit" style="left:72px;top:300px;width:48px;height:48px"></div>
      <svg class="car-icon" style="left:14px;top:330px"><use href="#car"/></svg>
      <svg class="car-icon" style="left:150px;top:360px"><use href="#car"/></svg>
    </article>

    <article class="panel">
      <div class="claim">…mit dem Meer an Möglichkeiten<em>…you won't miss the sea of options</em></div>
      <div class="offer" style="top:100px">
        <div class="offer__bar"></div><div class="offer__tag">Erlebnisprobefahrt</div>
        <div class="photo photo--car" role="img" aria-label="Elektroauto auf einer Landstraße"></div>
        <div class="offer__info"><div class="offer__title">Adventure test e-drive</div><p class="txt">Diverse Modelle stehen für Ihr besonderes Erlebnis zur Verfügung.</p><p class="txt txt--en">Many car models at your disposal.</p><div class="offer__price"><small>ab / from</small>29,00 EUR</div></div>
      </div>
      <div class="offer" style="top:226px">
        <div class="offer__bar"></div><div class="offer__tag">Miete ein e-bike</div>
        <div class="photo photo--bike" role="img" aria-label="Elektrofahrrad im Grünen"></div>
        <div class="offer__info"><div class="offer__title">Rent a e-bike</div><p class="txt">Einfach mal raus – bequem per eBike</p><p class="txt txt--en">Just get out – but comfortable with your ebike</p><div class="offer__price"><small>ab / from</small>9,00 EUR</div></div>
      </div>
    </article>
  </section>

</div>
</body>
</html>
```